Ward Compass Business Card Design*

We need a business card design for our company Ward Compass. Our company is specialized in providing online consulting services regarding medical institutions, hospitals and doctors. We work with patients worldwide looking to choose between healthcare providers. We have a website you may use as a reference, where we list doctors and clinics worldwide. So we target Medical providers as well as patients worldwide.
Target Market(s)
Medical Providers and patients around the world
Industry/Entity Type
Medical
Contact Information for Business Card
Salma Derkaoui
CEO
+90 612 348 2071
info@wardcompass-example.com
www.wardcompass-example.com
14 Annakhil 3 H.R.B. Rabat, Morocco
Requirements
Must have
- Company logo/name on one full side, personal info and smaller logo and company name on the other side.
Nice to have
- Smart and elegant design

```html
<!DOCTYPE html>
<html lang="en">
<head>
<meta charset="utf-8">
<title>Ward Compass – Business Card</title>
<link rel="stylesheet" href="https://fonts.googleapis.com/css2?family=Montserrat:wght@600&family=Roboto:wght@300;400;700&display=swap">
<style>
  :root {
    --navy: #15365f;
    --grey: #8a8a8a;
    --white: #ffffff;
    --ink: #444444;
    --backdrop: #e9eaec;
  }
  * { box-sizing: border-box; margin: 0; padding: 0; }
  html, body { width: 1200px; height: 900px; overflow: hidden; }
  body {
    background: var(--backdrop);
    font-family: "Roboto", Arial, sans-serif;
    position: relative;
  }
  .card {
    position: absolute;
    left: 250px;
    width: 700px;
    height: 400px;
    background: var(--white);
    box-shadow: 0 2px 10px rgba(0,0,0,0.12);
    overflow: hidden;
  }
  .card--front { top: 35px; }
  .card--back { top: 465px; }

  .brand {
    display: flex;
    align-items: center;
    gap: 14px;
  }
  .brand__dot {
    border-radius: 50%;
    background: var(--navy);
    flex: none;
  }
  .brand__name {
    font-family: "Montserrat", Arial, sans-serif;
    font-weight: 600;
    color: var(--navy);
    text-transform: uppercase;
    letter-spacing: 1px;
    white-space: nowrap;
  }

  .card--front .brand {
    position: absolute;
    left: 0; right: 0; top: 140px;
    justify-content: center;
  }
  .card--front .brand__dot { width: 56px; height: 56px; }
  .card--front .brand__name { font-size: 44px; }
  .front__web {
    position: absolute;
    left: 0; right: 0; top: 250px;
    text-align: center;
    font-size: 17px;
    font-weight: 300;
    letter-spacing: 6px;
    color: var(--ink);
  }

  .back__shapes { position: absolute; inset: 0; }
  .card--back .brand {
    position: absolute;
    left: 40px; top: 150px;
  }
  .card--back .brand__dot { width: 40px; height: 40px; }
  .card--back .brand__name { font-size: 31px; }

  .person {
    position: absolute;
    left: 48px; bottom: 26px;
    color: var(--white);
  }
  .person__name { font-size: 30px; font-weight: 700; line-height: 1.1; }
  .person__role { font-size: 15px; font-weight: 300; margin-top: 4px; }

  .contact {
    position: absolute;
    right: 28px; top: 120px;
    color: var(--white);
    text-align: right;
    font-size: 13px;
    font-weight: 300;
    line-height: 1.5;
  }
  .contact__rule {
    display: block;
    width: 26px; height: 2px;
    background: var(--white);
    margin: 8px 0 8px auto;
  }
  .contact__line { display: flex; justify-content: flex-end; align-items: center; gap: 8px; }
  .contact__icon { width: 14px; height: 14px; flex: none; }
</style>
</head>
<body>

<section class="card card--front">
  <div class="brand">
    <span class="brand__dot"></span>
    <span class="brand__name">Ward Compass</span>
  </div>
  <p class="front__web">www.wardcompass-example.com</p>
</section>

<section class="card card--back">
  <svg class="back__shapes" width="700" height="400" viewBox="0 0 700 400">
    <path d="M548,0 L700,0 L700,400 L0,400 L0,305 C260,295 505,200 548,0 Z" fill="var(--navy)"/>
    <path d="M506,0 L530,0 C492,200 255,288 0,296 L0,291 C240,282 468,190 506,0 Z" fill="var(--grey)"/>
    <rect x="0" y="330" width="10" height="55" fill="var(--white)"/>
  </svg>

  <div class="brand">
    <span class="brand__dot"></span>
    <span class="brand__name">Ward Compass</span>
  </div>

  <div class="person">
    <p class="person__name">Salma Derkaoui</p>
    <p class="person__role">CEO</p>
  </div>

  <div class="contact">
    <p>14 Annakhil</p>
    <p>3 H.R.B. Rabat, Morocco</p>
    <span class="contact__rule"></span>
    <p class="contact__line">+90 612 348 2071
      <svg class="contact__icon" viewBox="0 0 16 16"><circle cx="8" cy="8" r="8" fill="var(--white)"/><path d="M5,4 L7,4 L7.5,6.5 L6.5,7.3 C7,8.6 7.6,9.2 8.8,9.6 L9.6,8.6 L12,9.2 L12,11 C8,11.5 4.5,8 5,4 Z" fill="var(--navy)"/></svg>
    </p>
    <p class="contact__line">info@wardcompass-example.com
      <svg class="contact__icon" viewBox="0 0 16 16"><rect x="1" y="3" width="14" height="10" fill="var(--white)"/><path d="M1.5,3.5 L8,9 L14.5,3.5" fill="none" stroke="var(--navy)" stroke-width="1.2"/></svg>
    </p>
    <p class="contact__line">www.wardcompass-example.com
      <svg class="contact__icon" viewBox="0 0 16 16"><circle cx="8" cy="8" r="8" fill="var(--white)"/><circle cx="8" cy="8" r="5" fill="none" stroke="var(--navy)" stroke-width="1"/><path d="M3,8 H13 M8,3 C5.5,6 5.5,10 8,13 M8,3 C10.5,6 10.5,10 8,13" fill="none" stroke="var(--navy)" stroke-width="1"/></svg>
    </p>
  </div>
</section>

</body>
</html>
```